Specialized Personal Trainer Needs a Business Card Design

I need a business card design for my personal training business called Tall Oak Fitness. I have my Human Kinetics degree in Exercise Science from the Halvern Ridge University as well as an extra certification from NBEP (National Board of Exercise Practice). I work as a Cardiac Rehab Exercise Specialist and personal trainer giving specialized exercise prescriptions to those that have different heart conditions as well as work with the general population in weight loss, strength and conditioning, getting/staying fit.
Updates

I decided that I wanted a logo (as I did not have one before I submitted my project for a business card) so I am submitting a project to get a logo done and then I will decide on a business card, hopefully being able to use one of the designs already submitted.  My apologies for doing this backwards.  I am new to this so I appreciate your patience.

Thank you.

Hi, I have just created a project for a logo design (I realized I needed a logo and I should've done that first..oops!), please feel free to participate.  Once I receive a logo I like I will finalize my business card project and hopefully incorporate it into one of your business card designs. 

Thank you!

Target Market(s)

Business professionals

Industry/Entity Type

Personal Trainer

Requirements
Must have
• My name with my info:
Celia R. Dunhill (BHK)
NBEP Certified Clinical Exercise Specialist & Personal Trainer
celia.dunhill@talloakfitness.example
Cell: 604-358-4170

Please make it double sided.
Nice to have
• An image that represents cardiac and general fitness training.

```html
<!DOCTYPE html>
<html lang="en">
<head>
<meta charset="utf-8">
<title>Tall Oak Fitness — Business Card</title>
<link href="https://fonts.googleapis.com/css2?family=Fira+Sans:wght@300;500;600&display=swap" rel="stylesheet">
<style>
  :root {
    --backdrop: #000000;
    --card: #ffffff;
    --brand-blue: #41bfee;
    --text-grey: #8a8a8a;
    --card-edge: #d8d8d8;
  }
  * { margin: 0; padding: 0; box-sizing: border-box; }
  html, body {
    width: 1200px;
    height: 648px;
    overflow: hidden;
    background: var(--backdrop);
  }
  .canvas {
    position: relative;
    width: 1200px;
    height: 648px;
    font-family: "Fira Sans", "Helvetica Neue", Arial, sans-serif;
  }
  .card {
    position: absolute;
    left: 373px;
    width: 435px;
    height: 241px;
    background: var(--card);
  }
  .card--front { top: 75px; }
  .card--back { top: 325px; border-right: 1px solid var(--card-edge); }

  .brand {
    position: absolute;
    left: 0;
    right: 0;
    top: 70px;
    display: flex;
    flex-direction: column;
    align-items: center;
    gap: 20px;
  }
  .brand__mark {
    width: 88px;
    height: 88px;
    border-radius: 50%;
    background: var(--brand-blue);
  }
  .brand__name {
    font-size: 23px;
    line-height: 26px;
    font-weight: 600;
    color: var(--text-grey);
  }

  .contact {
    position: absolute;
    left: 26px;
    top: 72px;
    font-size: 17.5px;
    line-height: 22.5px;
    color: var(--text-grey);
  }
  .contact__name {
    color: var(--brand-blue);
    font-weight: 500;
  }
  .contact__title,
  .contact__phone { font-weight: 600; }
  .contact__email { font-weight: 300; }
</style>
</head>
<body>
  <main class="canvas">
    <section class="card card--front" aria-label="Card front">
      <div class="brand">
        <span class="brand__mark" aria-hidden="true"></span>
        <span class="brand__name">tall oak fitness</span>
      </div>
    </section>

    <section class="card card--back" aria-label="Card back">
      <div class="contact">
        <p class="contact__name">Celia R. Dunhill (BHK)</p>
        <p class="contact__title">NBEP Certified Clinical Exercise<br>Specialist &amp; Personal Trainer</p>
        <p class="contact__email">celia.dunhill@talloakfitness.example</p>
        <p class="contact__phone">Cell: 604-358-4170</p>
      </div>
    </section>
  </main>
</body>
</html>
```